Feature Nomination Banner

Create a 600 x 160 banner advertisement for Counsel Ledger Quarterly’s feature story nominations. We’ve included the Counsel Ledger Quarterly logo (black and white versions) for inclusion.
Headline: Now Accepting Nominations for 2024 Features
Nominate an Outstanding Lawyer or Law Firm Today!

```html
<!DOCTYPE html>
<html lang="en">
<head>
<meta charset="UTF-8">
<title>Counsel Ledger Quarterly – Feature Nominations Banner</title>
<link rel="stylesheet" href="https://fonts.googleapis.com/css2?family=Archivo:wght@400;700;800&family=Inter:wght@300;500&display=swap">
<style>
  :root {
    --page: #ffffff;
    --banner-light: #f7f7f6;
    --banner-mid: #ededeb;
    --ink-brown: #473c27;
    --gold: #b99c62;
    --logo-ink: #111111;
    --photo-warm: #d8c3ab;
    --photo-soft: #ece3d8;
  }
  * { margin: 0; padding: 0; box-sizing: border-box; }
  html, body {
    width: 1200px;
    height: 1200px;
    overflow: hidden;
    background: var(--page);
  }
  .canvas {
    position: relative;
    width: 1200px;
    height: 1200px;
    background: var(--page);
  }
  .banner {
    position: absolute;
    left: 0;
    top: 436px;
    width: 1200px;
    height: 318px;
    overflow: hidden;
    background: linear-gradient(90deg, var(--banner-mid) 0%, var(--banner-light) 45%, var(--banner-light) 70%, var(--banner-mid) 100%);
  }
  .brand {
    position: absolute;
    left: 54px;
    top: 64px;
    font-family: "Archivo", Arial, sans-serif;
    font-weight: 700;
    font-size: 23px;
    letter-spacing: 0.4px;
    text-transform: uppercase;
    color: var(--logo-ink);
  }
  .headline {
    position: absolute;
    left: 47px;
    top: 140px;
    font-family: "Archivo", Arial, sans-serif;
    font-weight: 800;
    font-size: 42px;
    line-height: 47px;
    letter-spacing: -0.4px;
    text-transform: uppercase;
    color: var(--ink-brown);
  }
  .subline {
    position: absolute;
    left: 47px;
    top: 240px;
    font-family: "Inter", Arial, sans-serif;
    font-weight: 300;
    font-size: 26px;
    letter-spacing: -0.3px;
    color: var(--gold);
  }
  .feature-photo {
    position: absolute;
    left: 745px;
    top: 0;
    width: 370px;
    height: 318px;
    background: linear-gradient(180deg, var(--photo-soft) 0%, var(--photo-warm) 100%);
  }
</style>
</head>
<body>
  <div class="canvas">
    <section class="banner">
      <div class="brand">Counsel Ledger Quarterly</div>
      <h1 class="headline">Now Accepting Nominations<br>for 2024 Features</h1>
      <p class="subline">Nominate an Outstanding Lawyer or Law Firm Today!</p>
      <div class="feature-photo" role="img" aria-label="Photo of a bronze Lady Justice statue holding scales, with a wooden gavel and a stack of books on a light table"></div>
    </section>
  </div>
</body>
</html>
```